Two-Sided Flyer - Architectural and Engineering Firm

Looking for a two-sided flyer that can be used at trade shows and initial meetings with new prospective clients that will highlight the services of our company as well as project photos of the type of work we do. You can find information and portfolio photos for your design ideas on our website at www.hollisfrenwickadair.com

Target Market(s)

K-12 School Corporations

Industry/Entity Type

Architectural

Colors

Designer to choose colors to be used in the design.

Requirements
Must have
• Company logo, project photos that highlight the work we do, contact information, brief highlight of services we offer

```html
<!DOCTYPE html>
<html lang="en">
<head>
<meta charset="utf-8">
<title>Hollis-Frenwick-Adair Two-Sided Flyer</title>
<link href="https://fonts.googleapis.com/css2?family=Questrial&display=swap" rel="stylesheet">
<style>
  :root {
    --backdrop: #d3e4e2;
    --paper: #efefef;
    --paper-edge: #e4e4e4;
    --navy: #3a4e5f;
    --brown: #8c5a45;
    --brown-dark: #7a4a36;
    --white: #ffffff;
    --sky-top: #2a4fb8;
    --sky-low: #8fb0d9;
    --brick: #b9a58f;
    --grass: #6f9a3c;
  }
  * { margin: 0; padding: 0; box-sizing: border-box; }
  html, body { width: 1200px; height: 799px; overflow: hidden; }
  body {
    background: var(--backdrop);
    font-family: "Questrial", "Century Gothic", sans-serif;
    position: relative;
  }
  .page {
    position: absolute;
    top: 104px;
    width: 422px;
    height: 597px;
    background: linear-gradient(180deg, var(--paper-edge) 0%, var(--paper) 40%, var(--paper) 100%);
    overflow: hidden;
  }
  .page--front { left: 139px; }
  .page--back { left: 635px; }

  .brand {
    position: absolute;
    left: 17px;
    top: 22px;
    display: flex;
    align-items: center;
    gap: 6px;
  }
  .brand__dot {
    width: 14px; height: 14px;
    border-radius: 50%;
    background: var(--navy);
  }
  .brand__name {
    color: var(--brown);
    font-size: 11.5px;
    letter-spacing: 0.3px;
  }

  .section-title {
    position: absolute;
    left: 17px;
    top: 70px;
    color: var(--brown);
    font-size: 11px;
  }

  .about {
    position: absolute;
    left: 17px;
    top: 89px;
    width: 404px;
    color: var(--brown);
  }
  .about__heading {
    font-size: 8.4px;
    text-decoration: underline;
    text-underline-offset: 1.5px;
    margin-bottom: 1.5px;
  }
  .about__text {
    font-size: 7px;
    line-height: 9.1px;
    margin-bottom: 13px;
  }
  .about__text--tapered { white-space: nowrap; }

  .front-art { position: absolute; inset: 0; }

  .photo-circle {
    position: absolute;
    border-radius: 50%;
  }
  .photo-circle--elementary {
    left: 25px; top: 315px; width: 172px; height: 172px;
    background: linear-gradient(180deg, var(--sky-top) 0%, #4f6ec4 35%, #a89880 55%, var(--grass) 72%, #7c7a74 100%);
  }
  .photo-circle--middle {
    left: 208px; top: 336px; width: 258px; height: 258px;
    background: linear-gradient(180deg, #8fb2dc 0%, #cfdbea 25%, var(--brick) 45%, #8a7d70 62%, #b3b5b7 75%, #7d8a4d 100%);
  }

  .services {
    position: absolute;
    left: 13px;
    top: 489px;
    color: var(--white);
  }
  .services__title { font-size: 13px; margin-bottom: 9px; }
  .services__list { list-style: none; padding-left: 4px; }
  .services__list li { font-size: 11px; line-height: 11.9px; }

  .portfolio-title {
    position: absolute;
    left: 16px;
    top: 69px;
    color: var(--brown);
    font-size: 13px;
  }
  .category {
    position: absolute;
    left: 0; width: 422px;
    text-align: center;
    color: var(--brown);
    font-size: 10px;
    letter-spacing: 0.3px;
  }
  .project-photo {
    position: absolute;
    height: 80px;
  }
  .project-photo--left { left: 0; width: 203px; border-radius: 0 8px 8px 0; }
  .project-photo--right { left: 215px; width: 207px; border-radius: 8px 0 0 8px; }

  .tone-library { background: linear-gradient(180deg, #d8d0c2 0%, #b99a78 45%, #6d6a5c 100%); }
  .tone-classroom { background: linear-gradient(180deg, #e2e2de 0%, #c9c9c6 50%, #5f5b59 100%); }
  .tone-exterior { background: linear-gradient(180deg, #0e2f9c 0%, #2a52c0 50%, #c9bd9c 72%, #3a6bb4 100%); }
  .tone-science { background: linear-gradient(180deg, #eeeeea 0%, #9a6a45 50%, #3d3b3a 100%); }
  .tone-cafeteria { background: linear-gradient(180deg, #f0efec 0%, #d7d4cf 50%, #2c2c2c 100%); }
  .tone-media { background: linear-gradient(180deg, #3c4c78 0%, #9a6e52 45%, #b67a5a 75%, #3c3d44 100%); }
  .tone-conference { background: linear-gradient(180deg, #f2f2f2 0%, #c8383a 45%, #ebe8e6 70%, #4a4f60 100%); }
  .tone-lobby { background: linear-gradient(180deg, #f1f1f1 0%, #cdd4da 45%, #6e4a34 75%, #3e3e3e 100%); }

  .back-footer { position: absolute; left: 0; top: 0; }

  .contact {
    position: absolute;
    color: var(--white);
    font-size: 7.4px;
    line-height: 9.2px;
  }
  .contact--intro { left: 16px; top: 521px; width: 395px; }
  .contact--address {
    left: 16px; top: 552px;
    border-left: 1px solid var(--white);
    padding: 1px 0 2px 6px;
    line-height: 10.2px;
  }
  .contact--lines {
    left: 261px; top: 552px;
    border-left: 1px solid var(--white);
    padding: 1px 0 2px 6px;
    line-height: 10.2px;
  }
</style>
</head>
<body>

  <section class="page page--front" aria-label="Flyer front: about and services">
    <svg class="front-art" width="422" height="597" viewBox="0 0 422 597" aria-hidden="true">
      <path d="M422,242 C360,300 290,345 200,366 C120,384 55,375 0,378 L0,597 L422,597 Z" fill="var(--navy)"/>
    </svg>

    <div class="brand">
      <span class="brand__dot"></span>
      <span class="brand__name">HOLLIS·FRENWICK·ADAIR</span>
    </div>

    <h2 class="section-title">About Us:</h2>

    <div class="about">
      <h3 class="about__heading">Educational Facility Design Focus Since 1969</h3>
      <p class="about__text">Early in our history, Hollis-Frenwick-Adair began delivering high quality, K-12 educational facility designs to school districts across Northern Indiana. Through the commitment of our directly involved principal owners and the collective efforts of our dedicated Architectural and Engineering staff, Hollis-Frenwick-Adair has dutifully and successfully continued to serve Indiana K-12 school clients across the state for the last 50 years running.</p>

      <h3 class="about__heading">Actively Involved With K-12 Education Community</h3>
      <p class="about__text">At Hollis-Frenwick-Adair, we take great pride in ensuring that our staff is on the forefront of discussions and the latest hot topics among the Indiana K-12 school community as it relates to education and school facility design. As a member of ISPA, ISFA, IEBA and ISLC, Hollis-Frenwick-Adair stays actively engaged with educators and school administrators across the State of Indiana to ensure that our designs are innovative, functional, and relevant to our clients.</p>

      <h3 class="about__heading">The HFA Experience</h3>
      <p class="about__text about__text--tapered">All in all, there is no Architectural or Engineering firm serving Northern Indiana that has more collective<br>experience in K-12 education facility design than Hollis-Frenwick-Adair.&nbsp; Our integrity and reputation<br>for providing clear, honest, and direct communication with both clients and building contractors<br>throughout the design and construction processes is second to none.&nbsp; These are the qualities<br>that have allowed us to build lasting relationships with over 50 school corporations that trust<br>us to serve them.&nbsp; At Hollis-Frenwick-Adair, we strive to combine our educational space<br>design experience with the best practices of educators and school administrators<br>across Indiana to help in developing the leaders of tomorrow.</p>
    </div>

    <div class="photo-circle photo-circle--elementary" role="img" aria-label="Photo of an elementary school exterior at dusk with lit windows, lawn and a curving drive"></div>
    <div class="photo-circle photo-circle--middle" role="img" aria-label="Photo of a middle school main entrance with brick facade and blue signage panel"></div>

    <div class="services">
      <h2 class="services__title">Our Services:</h2>
      <ul class="services__list">
        <li>- Architectural</li>
        <li>- Engineering</li>
        <li>- Pre-Design</li>
        <li>- Extended</li>
        <li>- Project Delivery</li>
        <li>- Other</li>
      </ul>
    </div>
  </section>

  <section class="page page--back" aria-label="Flyer back: portfolio and contact">
    <svg class="back-footer" width="422" height="597" viewBox="0 0 422 597" aria-hidden="true">
      <path d="M0,513 C140,506 300,500 422,488 L422,597 L0,597 Z" fill="var(--navy)"/>
    </svg>

    <div class="brand">
      <span class="brand__dot"></span>
      <span class="brand__name">HOLLIS·FRENWICK·ADAIR</span>
    </div>

    <h2 class="portfolio-title">Our Portfoilio:</h2>

    <h3 class="category" style="top:90px">Elementary Schools</h3>
    <div class="project-photo project-photo--left tone-library" style="top:110px" role="img" aria-label="Photo of an elementary school media center with bookshelves"></div>
    <div class="project-photo project-photo--right tone-classroom" style="top:110px" role="img" aria-label="Photo of an elementary classroom with red chairs and storage cabinets"></div>

    <h3 class="category" style="top:195px">Intermediate &amp; Jr High Schools</h3>
    <div class="project-photo project-photo--left tone-exterior" style="top:216px" role="img" aria-label="Photo of an intermediate school exterior under a deep blue sky with a flagpole"></div>
    <div class="project-photo project-photo--right tone-science" style="top:216px" role="img" aria-label="Photo of a science lab with black-top benches and wood cabinets"></div>

    <h3 class="category" style="top:300px">Jr &amp; Sr High Schools</h3>
    <div class="project-photo project-photo--left tone-cafeteria" style="top:319px" role="img" aria-label="Photo of a high school cafeteria with rows of tables and a flag on the wall"></div>
    <div class="project-photo project-photo--right tone-media" style="top:319px" role="img" aria-label="Photo of a high school library with bookshelves and round tables"></div>

    <h3 class="category" style="top:405px">Commercial</h3>
    <div class="project-photo project-photo--left tone-conference" style="top:422px" role="img" aria-label="Photo of a conference room with red chairs around a large table"></div>
    <div class="project-photo project-photo--right tone-lobby" style="top:422px" role="img" aria-label="Photo of a bright office lobby with a reception desk and glass walls"></div>

    <p class="contact contact--intro">For general information or questions about Hollis-Frenwick-Adair, please email us at inquiry@hollisfrenwickadair.com or call 555-014-2290.</p>

    <address class="contact contact--address" style="font-style:normal">
      Hollis-Frenwick-Adair<br>
      Architects &amp; Engineers<br>
      418 Meadowline Commerce Park<br>
      Lindenport, IN 46099
    </address>

    <p class="contact contact--lines">
      Tel: (555) 014 2290<br>
      Fax: (555) 014 2291<br>
      inquiry@hollisfrenwickadair.com<br>
      www.hollisfrenwickadair.com
    </p>
  </section>

</body>
</html>
```